Flyer Design Project

asphalt paving company needs 3 designs for inserts to place inside presentation folder. I will up load samples of basic concept and information required but needs to be completely redesigned. Looking for professional modern look.

Industry/Entity Type

It Company

```html
<!DOCTYPE html>
<html lang="en">
<head>
<meta charset="utf-8">
<title>Our Services</title>
<link href="https://fonts.googleapis.com/css2?family=PT+Sans:wght@400;700&display=swap" rel="stylesheet">
<style>
  :root {
    --orange-deep: #e5620f;
    --orange: #f08a1c;
    --yellow: #f7c623;
    --band: #f4c417;
    --cream-top: #ffffff;
    --cream-bottom: #fcf0b0;
    --ink: #1f1f1f;
    --bullet: #e27845;
    --dots: #6b6b6b;
  }
  * { margin: 0; padding: 0; box-sizing: border-box; }
  html, body { width: 853px; height: 1200px; overflow: hidden; background: #fff; }
  .flyer {
    position: relative; width: 853px; height: 1200px; overflow: hidden;
    font-family: "PT Sans", Arial, sans-serif; color: var(--ink);
    background: #fff;
  }
  .header {
    position: absolute; left: 0; top: 0; width: 853px; height: 155px;
    background: linear-gradient(180deg, var(--orange-deep) 0%, var(--orange) 40%, var(--yellow) 100%);
    border-bottom: 4px solid #111;
  }
  .header-title {
    position: absolute; left: 57px; top: 44px;
    font-size: 45px; font-weight: 400; letter-spacing: 0.5px; color: var(--ink);
  }
  .header-badge { position: absolute; left: 700px; top: 0; width: 140px; height: 140px; }

  .section {
    position: absolute; left: 0; width: 853px;
    background: linear-gradient(180deg, var(--cream-top) 0%, var(--cream-bottom) 100%);
  }
  .section--paving { top: 159px; height: 255px; }
  .section--concrete { top: 422px; height: 237px; }
  .section--ada { top: 668px; height: 249px; }
  .section--management { top: 926px; height: 247px; }
  .band { position: absolute; left: 0; width: 853px; background: var(--band); }
  .band--1 { top: 414px; height: 8px; }
  .band--2 { top: 659px; height: 9px; }
  .band--3 { top: 917px; height: 9px; }
  .band--foot { top: 1173px; height: 27px; }

  .photo {
    position: absolute; width: 234px; height: 234px; border-radius: 50%;
    border: 10px solid var(--band);
    box-shadow: 0 2px 6px rgba(0,0,0,0.25);
  }
  .photo--paving { left: 36px; top: 160px; background: linear-gradient(180deg, #b9d3ea 0%, #d9dde0 40%, #4a4a4c 60%, #2e2e30 100%); }
  .photo--concrete { left: 589px; top: 422px; background: linear-gradient(180deg, #c8d6e2 0%, #9aa3a6 28%, #6d665d 45%, #4f4a43 100%); }
  .photo--ada { left: 37px; top: 678px; background: linear-gradient(160deg, #d6e1ea 0%, #c5c8cc 30%, #3c3d40 50%, #2a2b2e 100%); }
  .photo--demolition { left: 586px; top: 939px; background: linear-gradient(180deg, #8f9396 0%, #c9cccd 40%, #a8a9a8 70%, #6a6862 100%); }

  .lines { position: absolute; left: 0; top: 0; width: 853px; height: 1200px; pointer-events: none; }

  .service-list { position: absolute; list-style: none; font-size: 20px; font-weight: 700; line-height: 26.7px; }
  .service-list li { position: relative; padding-left: 22px; }
  .service-list li::before {
    content: ""; position: absolute; left: 0; top: 9px; width: 11px; height: 11px;
    border-radius: 50%; background: var(--bullet);
  }
  .service-list--wide li { padding-left: 29px; }
  .list--paving-a { left: 419px; top: 232px; }
  .list--paving-b { left: 640px; top: 232px; }
  .list--concrete { left: 58px; top: 478px; }
  .list--ada { left: 608px; top: 744px; }
  .list--management { left: 58px; top: 984px; }
</style>
</head>
<body>
<div class="flyer">
  <header class="header">
    <h1 class="header-title">OUR SERVICES</h1>
    <svg class="header-badge" viewBox="0 0 140 140" role="img" aria-label="Round badge with a hammer and wrench tool icon">
      <circle cx="70" cy="64" r="62" fill="#c9c9c9"/>
      <circle cx="70" cy="64" r="55" fill="#8a8a8a"/>
      <circle cx="70" cy="64" r="48" fill="#ee7d16"/>
      <circle cx="70" cy="64" r="40" fill="#e46812"/>
    </svg>
  </header>

  <section class="section section--paving"></section>
  <div class="band band--1"></div>
  <section class="section section--concrete"></section>
  <div class="band band--2"></div>
  <section class="section section--ada"></section>
  <div class="band band--3"></div>
  <section class="section section--management"></section>
  <div class="band band--foot"></div>

  <svg class="lines" viewBox="0 0 853 1200" aria-hidden="true">
    <g fill="none" stroke="var(--dots)" stroke-width="1.6" stroke-dasharray="1.5 2.5">
      <path d="M182 186 H703 V214"/>
      <path d="M63 458 V461 H635"/>
      <path d="M257 729 H613 V738"/>
      <path d="M63 974 V970 H614"/>
    </g>
    <g fill="var(--bullet)">
      <circle cx="182" cy="186" r="4"/>
      <circle cx="703" cy="217" r="5.5"/>
      <circle cx="63" cy="463" r="5.5"/>
      <circle cx="613" cy="741" r="5.5"/>
      <circle cx="63" cy="977" r="5.5"/>
    </g>
  </svg>

  <div class="photo photo--paving" role="img" aria-label="Photo of a road roller compacting fresh asphalt in a parking lot"></div>
  <div class="photo photo--concrete" role="img" aria-label="Photo of a crew finishing a concrete slab beside traffic cones"></div>
  <div class="photo photo--ada" role="img" aria-label="Photo of freshly striped parking lot with crosswalk markings"></div>
  <div class="photo photo--demolition" role="img" aria-label="Photo of milling machinery removing old pavement amid dust"></div>

  <ul class="service-list list--paving-a">
    <li>New Grade/Pave</li>
    <li>Remove &amp; Replace</li>
    <li>Fabric Overlays</li>
    <li>Skin Patching</li>
  </ul>
  <ul class="service-list list--paving-b">
    <li>Seal Coating</li>
    <li>Road Slurry</li>
    <li>Trench Repairs</li>
    <li>Crack Seal</li>
  </ul>
  <ul class="service-list service-list--wide list--concrete">
    <li>Concrete</li>
    <li>Truncated Domes</li>
    <li>Curbs</li>
    <li>Gutters</li>
    <li>Slabs</li>
  </ul>
  <ul class="service-list service-list--wide list--ada">
    <li>Striping/Signage</li>
    <li>ADA Upgrades</li>
    <li>ADA Ramps</li>
    <li>ADA Rails</li>
  </ul>
  <ul class="service-list service-list--wide list--management">
    <li>Free Estimates</li>
    <li>Permit Applications</li>
    <li>Construction Management</li>
    <li>Design</li>
    <li>Import &amp; Export</li>
    <li>Demolition</li>
  </ul>
</div>
</body>
</html>
```